My business is Property developing Stationary

I want business card and stationery. Please have the formate so I can edit details on card and stationary.

Please see my logo and on the back of the card I want it same red as my logo and I will provide copy that I want on the back of the card.

Also need an email signature

On the business card and email signature add below copy:
Project Management- Acquisitions- Syndicates- Joint Ventures

Target Market(s)

Property investors

Industry/Entity Type

Business

Requirements
Must have
• Reflect my Logo

```html
<!DOCTYPE html>
<html lang="en">
<head>
<meta charset="utf-8">
<title>Verano Property Developments – Stationery</title>
<link rel="stylesheet" href="https://fonts.googleapis.com/css2?family=Montserrat:wght@500;600;700;800&family=Open+Sans:wght@400&display=swap">
<style>
  :root {
    --brand-red: #ea1d24;
    --ink: #1c1c1c;
    --paper: #ffffff;
    --board: #8c8c8c;
    --window: #f1f1f1;
    --wood-dark: #5a4a40;
    --wood-light: #8a776a;
    --glass-dark: #6f6a66;
    --glass-light: #d9d4cf;
  }
  * { box-sizing: border-box; margin: 0; padding: 0; }
  html, body { width: 883px; height: 1200px; overflow: hidden; }
  body { position: relative; background: var(--board); font-family: "Open Sans", sans-serif; color: var(--ink); }

  .sheet { position: absolute; background: var(--paper); overflow: hidden; }

  .brand { position: absolute; line-height: 1; }
  .brand-name { font-family: "Montserrat", sans-serif; font-weight: 800; color: var(--brand-red); letter-spacing: 0.5px; display: block; }
  .brand-tag { font-family: "Montserrat", sans-serif; font-weight: 700; color: var(--ink); display: block; }

  .contact { position: absolute; font-family: "Montserrat", sans-serif; font-weight: 600; color: var(--ink); }
  .contact-row { display: flex; align-items: center; }
  .contact-row svg { flex: none; }

  /* Letterhead */
  .letterhead { left: 82px; top: 96px; width: 503px; height: 661px; }
  .letterhead .brand { left: 30px; top: 40px; }
  .letterhead .brand-name { font-size: 27px; }
  .letterhead .brand-tag { font-size: 9.5px; margin-top: 2px; padding-left: 12px; }
  .letterhead .contact { left: 315px; top: 30px; font-size: 7px; }
  .letterhead .contact-row { gap: 6px; margin-bottom: 9px; }
  .letter-body { position: absolute; left: 29px; top: 194px; width: 470px; font-size: 10.5px; line-height: 16px; white-space: nowrap; }
  .letter-body p { margin-bottom: 14px; }
  .letter-band { position: absolute; left: 0; bottom: 0; width: 160px; height: 35px; background: var(--brand-red); }

  /* Business card front */
  .card-front { left: 527px; top: 96px; width: 224px; height: 128px; }
  .card-front .brand { left: 36px; top: 48px; }
  .card-front .brand-name { font-size: 27px; }
  .card-front .brand-tag { font-size: 9.5px; margin-top: 2px; padding-left: 7px; }

  /* Business card back */
  .card-back { left: 527px; top: 236px; width: 224px; height: 128px; }
  .card-back .brand { right: 14px; top: 17px; text-align: right; }
  .card-back .brand-name { font-size: 15px; }
  .card-back .brand-tag { font-size: 5.5px; margin-top: 1px; }
  .card-back .shapes { position: absolute; left: 0; top: 0; }
  .card-person { position: absolute; left: 24px; top: 57px; color: var(--paper); font-family: "Montserrat", sans-serif; text-align: center; width: 62px; }
  .card-person .name { font-size: 9px; font-weight: 500; display: block; }
  .card-person .title { font-size: 5px; letter-spacing: 3px; display: block; margin-top: 1px; }
  .card-back .contact-left { left: 14px; top: 92px; font-size: 4px; }
  .card-back .contact-left .contact-row { gap: 3px; }
  .card-back .contact-right { left: 135px; top: 84px; font-size: 3.6px; color: var(--paper); }
  .card-back .contact-right .contact-row { gap: 3px; margin-bottom: 2px; }

  /* Open envelope */
  .envelope-open { left: 240px; top: 370px; width: 518px; height: 245px; }
  .envelope-open .flap { position: absolute; left: 0; top: 0; }
  .envelope-open .brand { left: 185px; top: 106px; }
  .envelope-open .brand-name { font-size: 27px; }
  .envelope-open .brand-tag { font-size: 9.5px; margin-top: 2px; padding-left: 13px; }

  /* Closed envelope */
  .envelope-front { left: 240px; top: 632px; width: 518px; height: 246px; }
  .envelope-front .brand { left: 47px; top: 44px; }
  .envelope-front .brand-name { font-size: 23px; }
  .envelope-front .brand-tag { font-size: 8.5px; margin-top: 2px; padding-left: 12px; }
  .envelope-front .contact { left: 46px; top: 155px; font-size: 5px; }
  .envelope-front .contact-row { gap: 5px; margin-bottom: 6px; }
  .address-window { position: absolute; left: 330px; top: 184px; width: 138px; height: 28px; border-radius: 8px; background: var(--window); }
  .envelope-rule { position: absolute; left: 17px; top: 226px; width: 485px; height: 6px; background: var(--brand-red); }

  /* Logo presentations */
  .showcase { position: absolute; top: 940px; height: 260px; }
  .showcase-wall { left: 0; width: 440px; background: linear-gradient(160deg, var(--wood-light), var(--wood-dark)); }
  .showcase-glass { left: 442px; width: 441px; background: linear-gradient(90deg, var(--glass-light), var(--glass-dark) 60%, var(--glass-light)); }
  .showcase .brand { left: 50%; top: 50%; transform: translate(-50%, -50%); text-align: center; }
  .showcase .brand-name { font-size: 62px; color: var(--paper); }
  .showcase .brand-tag { font-size: 22px; color: var(--paper); margin-top: 4px; }
</style>
</head>
<body>

<svg width="0" height="0" style="position:absolute">
  <defs>
    <symbol id="icon-pin" viewBox="0 0 12 12"><circle cx="6" cy="6" r="6" fill="#1c1c1c"/><path d="M6 2.6a2.2 2.2 0 0 0-2.2 2.2c0 1.7 2.2 4.2 2.2 4.2s2.2-2.5 2.2-4.2A2.2 2.2 0 0 0 6 2.6z" fill="#fff"/></symbol>
    <symbol id="icon-mail" viewBox="0 0 12 12"><circle cx="6" cy="6" r="6" fill="#1c1c1c"/><rect x="3" y="4" width="6" height="4.2" fill="#fff"/><path d="M3 4l3 2.4L9 4" stroke="#1c1c1c" stroke-width="0.6" fill="none"/></symbol>
    <symbol id="icon-phone" viewBox="0 0 12 12"><circle cx="6" cy="6" r="6" fill="#1c1c1c"/><path d="M4 3l1.2 1.6-.6.8a4 4 0 0 0 2 2l.8-.6L9 8l-.8 1C6 9 3 6 3 3.8z" fill="#fff"/></symbol>
    <symbol id="icon-web" viewBox="0 0 12 12"><circle cx="6" cy="6" r="6" fill="#1c1c1c"/><circle cx="6" cy="6" r="3" fill="none" stroke="#fff" stroke-width="0.7"/><path d="M3 6h6M6 3c-1.4 1.6-1.4 4.4 0 6M6 3c1.4 1.6 1.4 4.4 0 6" stroke="#fff" stroke-width="0.6" fill="none"/></symbol>
  </defs>
</svg>

<!-- Letterhead -->
<section class="sheet letterhead">
  <div class="brand"><span class="brand-name">VERANO</span><span class="brand-tag">Property Developments</span></div>
  <div class="contact">
    <div class="contact-row"><svg width="13" height="13"><use href="#icon-pin"/></svg><span>123 ANY STREET,ANY TOWN 1<br>YOUR COUNTRY</span></div>
    <div class="contact-row"><svg width="13" height="13"><use href="#icon-mail"/></svg><span style="font-size:6px">YOURNAME@YOURBUSINESS.COM</span></div>
    <div class="contact-row"><svg width="13" height="13"><use href="#icon-phone"/></svg><span style="font-size:6px">(123) 456-7890<br>(123) 456-7890</span></div>
    <div class="contact-row"><svg width="13" height="13"><use href="#icon-web"/></svg><span style="font-size:6px">WWW.YOURNAME.COM</span></div>
  </div>
  <div class="letter-body">
    <p>Dear [Recipient],</p>
    <p>We love the look of this stationery just the way it is. But you can add your own personal touch in<br>almost no time.</p>
    <p>On the Design tab of the ribbon, check out the Themes, Colors, and Fonts galleries to preview<br>different looks from a variety of choices.</p>
    <p>We’ve also created styles that let you match the formatting in this letter with just a click.<br>On the Home tab of the ribbon, check out the Styles gallery.</p>
    <p>Ready to add your digits? Now is the time to replace the sample text with your own contact<br>information.</p>
    <p>Warm regards,<br>Maren</p>
  </div>
  <div class="letter-band"></div>
</section>

<!-- Business card front -->
<section class="sheet card-front">
  <div class="brand"><span class="brand-name">VERANO</span><span class="brand-tag">Property Developments</span></div>
</section>

<!-- Business card back -->
<section class="sheet card-back">
  <svg class="shapes" width="224" height="128" viewBox="0 0 224 128">
    <polygon points="0,51 98,51 118,82 224,82 224,110 120,110 104,82 0,82" fill="#ea1d24"/>
  </svg>
  <div class="brand"><span class="brand-name">VERANO</span><span class="brand-tag">Property Developments</span></div>
  <div class="card-person"><span class="name">YOUR NAME</span><span class="title">TITLE</span></div>
  <div class="contact contact-left">
    <div class="contact-row"><svg width="5" height="5"><use href="#icon-pin"/></svg><span>123 ANY STREET,ANY TOWN 1201 US<br>YOUR COUNTRY</span></div>
  </div>
  <div class="contact contact-right">
    <div class="contact-row"><svg width="5" height="5"><use href="#icon-mail"/></svg><span>YOURNAME@YOURBUSINESS.COM</span></div>
    <div class="contact-row"><svg width="5" height="5"><use href="#icon-phone"/></svg><span>(123) 456-7890<br>(123) 456-7890</span></div>
    <div class="contact-row"><svg width="5" height="5"><use href="#icon-web"/></svg><span>WWW.YOURNAME.COM</span></div>
  </div>
</section>

<!-- Open envelope -->
<section class="sheet envelope-open">
  <svg class="flap" width="518" height="50" viewBox="0 0 518 50">
    <polygon points="0,0 518,0 500,48 20,48" fill="#ea1d24"/>
  </svg>
  <div class="brand"><span class="brand-name">VERANO</span><span class="brand-tag">Property Developments</span></div>
</section>

<!-- Closed envelope -->
<section class="sheet envelope-front">
  <div class="brand"><span class="brand-name">VERANO</span><span class="brand-tag">Property Developments</span></div>
  <div class="contact">
    <div class="contact-row"><svg width="9" height="9"><use href="#icon-pin"/></svg><span>123 ANY STREET,ANY TOWN 1201 US<br>YOUR COUNTRY</span></div>
    <div class="contact-row"><svg width="9" height="9"><use href="#icon-mail"/></svg><span>YOURNAME@YOURBUSINESS.COM</span></div>
    <div class="contact-row"><svg width="9" height="9"><use href="#icon-phone"/></svg><span>(123) 456-7890<br>(123) 456-7890</span></div>
    <div class="contact-row"><svg width="9" height="9"><use href="#icon-web"/></svg><span>WWW.YOURNAME.COM</span></div>
  </div>
  <div class="address-window"></div>
  <div class="envelope-rule"></div>
</section>

<!-- Logo presentations -->
<section class="showcase showcase-wall" role="img" aria-label="Brand name shown as raised lettering on a wooden wall">
  <div class="brand"><span class="brand-name">VERANO</span><span class="brand-tag">Property Developments</span></div>
</section>
<section class="showcase showcase-glass" role="img" aria-label="Brand name shown as frosted lettering on an office glass window">
  <div class="brand"><span class="brand-name">VERANO</span><span class="brand-tag">Property Developments</span></div>
</section>

</body>
</html>
```